Youth hostel in Barcelona needs an Advertisement for a university journal

We need an advertising design for a youth hostel in Barcelona that will be published in a journal for University students in the UK. We own two hostels in Barcelona, so we can host more than 150 people at the same time. We offer cheap accommodation (you can find beds for 8 pounds in the winter) with a lot of free services as wifi, full equipped kitchen, free activities, etc. We are not a party hostel, but English students look for party in Barcelona and some of them for cultural insights, so we need to attract all these people to come to the hostel (party and cultural).
I attach our logo (with the colors of the company), some pictures of our hostel and a picture of an advertisement that another hostel did. I also attach a picture that I found that I think is fresh and forces you to look what it is.

```html
<!DOCTYPE html>
<html lang="en">
<head>
<meta charset="utf-8">
<title>Casa Mirador Hostel – Experience Barcelona</title>
<link rel="stylesheet" href="https://fonts.googleapis.com/css2?family=Comfortaa:wght@300;400;700&display=swap">
<style>
  :root {
    --navy: #103a4f;
    --teal: #1f9e9b;
    --teal-light: #5fc4c0;
    --yellow: #f4c634;
    --red: #e2383c;
    --white: #ffffff;
    --photo-warm: #c98a6a;
    --photo-light: #efe0d4;
    --photo-dark: #5a3b2c;
  }
  * { margin: 0; padding: 0; box-sizing: border-box; }
  html, body { width: 1200px; height: 848px; overflow: hidden; background: var(--white); }
  .ad {
    position: relative;
    width: 1200px;
    height: 848px;
    overflow: hidden;
    font-family: "Comfortaa", sans-serif;
  }
  .hero-photo {
    position: absolute;
    inset: 0 0 240px 0;
    background:
      radial-gradient(circle at 30% 60%, rgba(255,120,160,.55) 0, transparent 18%),
      radial-gradient(circle at 48% 68%, rgba(90,200,220,.5) 0, transparent 16%),
      radial-gradient(circle at 62% 28%, rgba(255,210,80,.55) 0, transparent 20%),
      radial-gradient(circle at 80% 40%, rgba(120,70,50,.6) 0, transparent 30%),
      linear-gradient(120deg, var(--photo-light) 0%, var(--photo-warm) 45%, var(--photo-dark) 100%);
  }
  .brand {
    position: absolute;
    top: 24px;
    left: 26px;
    display: flex;
    align-items: center;
    gap: 12px;
    padding: 14px 20px;
    background: rgba(255,255,255,.9);
    border-radius: 10px;
  }
  .brand-dot { width: 34px; height: 34px; border-radius: 50%; background: var(--teal); }
  .brand-name { color: var(--navy); font-weight: 700; font-size: 26px; line-height: 1.1; }
  .bands { position: absolute; inset: 0; }
  .headline {
    position: absolute;
    left: 74px;
    top: 598px;
    color: var(--yellow);
    font-weight: 300;
    font-size: 74px;
    line-height: 1;
    white-space: nowrap;
  }
  .price-badge {
    position: absolute;
    left: 938px;
    top: 584px;
    width: 178px;
    height: 178px;
    border-radius: 50%;
    background: var(--red);
    color: var(--white);
    display: flex;
    flex-direction: column;
    align-items: center;
    padding-top: 30px;
  }
  .price-label { font-size: 16px; letter-spacing: 1px; line-height: 1; }
  .price-amount { font-size: 88px; font-weight: 400; line-height: 1; margin-top: 4px; }
  .price-unit { font-size: 15px; line-height: 1; align-self: flex-end; margin-right: 34px; margin-top: -6px; }
  .services {
    position: absolute;
    top: 726px;
    left: 0;
    width: 1200px;
    display: flex;
    justify-content: center;
    gap: 26px;
    list-style: none;
  }
  .service-icon {
    width: 46px; height: 46px;
    border-radius: 50%;
    background: var(--white);
    display: flex;
    align-items: center;
    justify-content: center;
  }
  .service-icon svg { width: 26px; height: 26px; }
  .website {
    position: absolute;
    top: 782px;
    left: 0;
    width: 1200px;
    text-align: center;
    color: var(--teal-light);
    font-size: 24px;
    letter-spacing: 3px;
  }
</style>
</head>
<body>
<main class="ad">
  <div class="hero-photo" role="img" aria-label="Photo of a young woman in colourful sunglasses blowing a handful of bright confetti"></div>

  <div class="brand">
    <span class="brand-dot"></span>
    <span class="brand-name">Casa Mirador</span>
  </div>

  <svg class="bands" width="1200" height="848" viewBox="0 0 1200 848" aria-hidden="true">
    <polygon points="0,640 1000,580 1200,565 1200,848 0,848" fill="var(--teal)"/>
    <polygon points="0,588 960,570 1000,698 0,698" fill="var(--navy)"/>
  </svg>

  <h1 class="headline">Experience Barcelona</h1>

  <div class="price-badge">
    <span class="price-label">BEDS FROM</span>
    <span class="price-amount">£8</span>
    <span class="price-unit">PP</span>
  </div>

  <ul class="services" aria-label="Hostel services">
    <li class="service-icon" aria-label="Wifi">
      <svg viewBox="0 0 30 30"><circle cx="8" cy="22" r="3" fill="var(--navy)"/><path d="M6 14a10 10 0 0 1 10 10M6 7a17 17 0 0 1 17 17" fill="none" stroke="var(--navy)" stroke-width="3.2"/></svg>
    </li>
    <li class="service-icon" aria-label="Luggage storage">
      <svg viewBox="0 0 30 30"><rect x="4" y="10" width="22" height="15" rx="2" fill="var(--navy)"/><path d="M11 10V6h8v4" fill="none" stroke="var(--navy)" stroke-width="2.5"/></svg>
    </li>
    <li class="service-icon" aria-label="Kitchen">
      <svg viewBox="0 0 30 30"><path d="M9 4v8M6 4v7a3 3 0 0 0 6 0V4M9 14v13M21 4c-3 2-4 7-4 11h4v12" fill="none" stroke="var(--navy)" stroke-width="2.6" stroke-linecap="round"/></svg>
    </li>
    <li class="service-icon" aria-label="Social">
      <svg viewBox="0 0 30 30"><circle cx="15" cy="15" r="8" fill="var(--navy)"/></svg>
    </li>
    <li class="service-icon" aria-label="Photos">
      <svg viewBox="0 0 30 30"><rect x="4" y="9" width="22" height="16" rx="3" fill="var(--navy)"/><rect x="11" y="6" width="8" height="4" fill="var(--navy)"/><circle cx="15" cy="17" r="4.5" fill="var(--white)"/></svg>
    </li>
  </ul>

  <p class="website">WWW.CASAMIRADORHOSTEL.COM</p>
</main>
</body>
</html>
```